Exciting opportunity to create logo and a label for our natural health brand.

About us

We are a customer centric health supplement brand who believes in natural medicine and high quality ingredients. We take a holistic approach to healthcare, with an eastern philosophy. We believe in being partners with our customers in their health care journey and are invested in their well being.

Our brand philosophy and values are attached (see Varro philosophy.png). Our personality traits are:

- Natural
- Fresh
- Modern
- Balanced (in a holistic sense)

Task breakdown

1. Design a fresh feeling logo for us
- We want it to represent our values and high quality ingredients. We would like the quality of the product to be reflected in the branding and have a high end feel.
- Logo text must include Varro Health Sciences
- We want the Varro to be the focus of the logo (see uploaded image Varro logo example.png)
The logo does not have to follow this layout, but we just want the Varro to stand out. Feel free to use your creative license on this!

2. Create an attractive label to go on the supplement bottle
- The designs need to be eye catching, give a sense of high end ingredients and natural products and tie in with the logo to give a joined up feel.
- We are selling our products online and need them to really stand out from the competition.
- See examples of labels and packaging we like (1 -7 label design).

The initial label we would like you to design would be for our product Calm Harbor. It is a product that assists in the management of Anxiety and stress. The label will appear on the bottle that holds the capsules for this supplement, see uploaded files (Example plain bottles.png). The bottles may be white as the picture shows or dark blue recyclable plastic or dark brown glass . We don't have the exact dimensions of the bottle yet, but I will follow up with these.

The label needs to include the following things:
1. The logo
2. The name of the product
3. The product is to help with the relief of Anxiety and Stress
4. Number of capsules the bottle contains
5. The back of the label should have
i) The ingredients
ii) Dosage
iii) Directions of use

Please use placeholder text where needed.

We look forward to seeing your design. Thank you.

```html
<!DOCTYPE html>
<html lang="en">
<head>
<meta charset="UTF-8">
<title>Varro Health Sciences – Calm Harbor Labels</title>
<link href="https://fonts.googleapis.com/css2?family=Bebas+Neue&family=Poppins:wght@300;400;500;600&display=swap" rel="stylesheet">
<style>
  :root {
    --page: #ffffff;
    --label: #efebdf;
    --ink: #2e2e2c;
    --ink-soft: #4a4a47;
    --leaf-light: #cfdcc6;
    --leaf-mid: #93b08c;
    --orange: #e8a448;
    --mauve: #b697a8;
    --blue: #5d91a7;
    --slate: #6c8787;
  }
  * { margin: 0; padding: 0; box-sizing: border-box; }
  html, body {
    width: 1200px; height: 621px; overflow: hidden;
    background: var(--page);
    font-family: "Poppins", sans-serif;
    color: var(--ink);
  }
  .label-set {
    width: 1200px; height: 621px;
    display: flex; justify-content: center; align-items: center; gap: 40px;
  }
  .label {
    position: relative;
    width: 252px; height: 300px;
    background: var(--label);
    box-shadow: 0 2px 10px rgba(0,0,0,0.08);
  }
  .brand {
    position: absolute; left: 43px; top: 22px;
    font-weight: 400; color: var(--ink);
  }
  .brand-name { font-size: 40px; line-height: 1; letter-spacing: -1px; }
  .brand-sub { font-size: 7.5px; letter-spacing: 1.2px; text-transform: uppercase; margin-top: 3px; }
  .leaf-art {
    position: absolute; left: 134px; top: 24px;
    width: 94px; height: 126px;
    border-radius: 60% 40% 55% 45%;
    background: radial-gradient(ellipse at 45% 60%, var(--leaf-mid) 0%, var(--leaf-light) 55%, rgba(239,235,223,0) 80%);
    opacity: 0.8;
  }
  .product-name {
    position: absolute; left: 42px; top: 160px;
    font-family: "Bebas Neue", sans-serif;
    font-size: 37px; line-height: 1; letter-spacing: 0.5px;
    color: var(--ink);
  }
  .formula {
    position: absolute; left: 36px; top: 206px;
    width: 186px; height: 20px;
    padding-left: 7px;
    font-size: 10px; letter-spacing: 0.8px; line-height: 20px;
    color: var(--ink-soft);
    background: linear-gradient(90deg, transparent 0%, var(--accent-soft) 12%, var(--accent-soft) 85%, transparent 100%);
  }
  .formula strong { font-weight: 500; color: var(--accent-text); }
  .claim {
    position: absolute; left: 43px; top: 232px;
    font-size: 10.5px; letter-spacing: 1px; line-height: 16px;
    text-transform: uppercase; color: var(--ink-soft);
  }
  .claim b { font-weight: 600; color: var(--ink); }
  .info-band {
    position: absolute; left: 0; right: 0; top: 271px; height: 18px;
    background: var(--accent);
    font-size: 8px; letter-spacing: 1px; line-height: 18px;
    padding-left: 43px; text-transform: uppercase; color: var(--band-text);
  }
  .label--orange { --accent: var(--orange); --accent-soft: rgba(232,164,72,0.35); --accent-text: #b26f17; --band-text: #5a3e12; }
  .label--mauve  { --accent: var(--mauve);  --accent-soft: rgba(182,151,168,0.3); --accent-text: #4a3a43; --band-text: #43363d; }
  .label--blue   { --accent: var(--blue);   --accent-soft: rgba(93,145,167,0.3);  --accent-text: #2d5668; --band-text: #1f3a46; }
  .label--slate  { --accent: var(--slate);  --accent-soft: rgba(108,135,135,0.3); --accent-text: #354848; --band-text: #263434; }
</style>
</head>
<body>
<main class="label-set">
  <article class="label label--orange">
    <div class="brand"><div class="brand-name">varro</div><div class="brand-sub">Health Sciences</div></div>
    <div class="leaf-art" role="img" aria-label="Botanical leaf sprig illustration"></div>
    <h1 class="product-name">CALM HARBOR</h1>
    <p class="formula">Vitamins · <strong>Minerals</strong> · Herbs</p>
    <p class="claim">Relief of<br><b>Anxiety</b> and <b>Stress</b></p>
    <p class="info-band">60 Capsules | Dietary Supplement</p>
  </article>
  <article class="label label--mauve">
    <div class="brand"><div class="brand-name">varro</div><div class="brand-sub">Health Sciences</div></div>
    <div class="leaf-art" role="img" aria-label="Botanical leaf sprig illustration"></div>
    <h1 class="product-name">CALM HARBOR</h1>
    <p class="formula">Vitamins · <strong>Minerals</strong> · Herbs</p>
    <p class="claim">Relief of<br><b>Anxiety</b> and <b>Stress</b></p>
    <p class="info-band">60 Capsules | Dietary Supplement</p>
  </article>
  <article class="label label--blue">
    <div class="brand"><div class="brand-name">varro</div><div class="brand-sub">Health Sciences</div></div>
    <div class="leaf-art" role="img" aria-label="Botanical leaf sprig illustration"></div>
    <h1 class="product-name">CALM HARBOR</h1>
    <p class="formula">Vitamins · <strong>Minerals</strong> · Herbs</p>
    <p class="claim">Relief of<br><b>Anxiety</b> and <b>Stress</b></p>
    <p class="info-band">60 Capsules | Dietary Supplement</p>
  </article>
  <article class="label label--slate">
    <div class="brand"><div class="brand-name">varro</div><div class="brand-sub">Health Sciences</div></div>
    <div class="leaf-art" role="img" aria-label="Botanical leaf sprig illustration"></div>
    <h1 class="product-name">CALM HARBOR</h1>
    <p class="formula">Vitamins · <strong>Minerals</strong> · Herbs</p>
    <p class="claim">Relief of<br><b>Anxiety</b> and <b>Stress</b></p>
    <p class="info-band">60 Capsules | Dietary Supplement</p>
  </article>
</main>
</body>
</html>
```